we need an experienced designer to design the tube for our toothpaste

Design guidelines:
1. On the front side, our product logo (‘Q2786’) should be prominent enough.
2. Our brand logo (‘quorlume’) could be small-size and it's just a trademark indeed.

Some information here for your reference:
1. The color of toothpaste cap is white.
2. We hope that the primary color in the design is blue.
3.‘F’ in ‘Q2786’ stands for ‘quorlume’ and ‘fluoride’.
4. We will use aluminum-plastic composite materials to make toothpaste tubes. In addition to the design, we also hope that you can make relevant suggestions on the special requirements of printing.

At last, we hope that you could submit both 2D design and 3D visual effects.

Attachments:

Colors
0094D4
00A9DD
6FCCEA
C7EBF8
E9F6FB

Requirements
Must have
• as attached

```html
<!DOCTYPE html>
<html lang="en">
<head>
<meta charset="utf-8">
<title>quorlume Orthodontic Toothpaste – Tube Artwork</title>
<link href="https://fonts.googleapis.com/css2?family=Montserrat:ital,wght@0,500;0,700;0,800;0,900;1,500;1,700&display=swap" rel="stylesheet">
<style>
  :root{
    --blue-deep:#0b5f8f;
    --blue-primary:#0094d4;
    --blue-bright:#00a9dd;
    --blue-soft:#6fccea;
    --blue-pale:#c7ebf8;
    --blue-mist:#e9f6fb;
    --ink:#111820;
    --white:#ffffff;
    --bg:#000000;
  }
  *{box-sizing:border-box;margin:0;padding:0}
  html,body{width:1200px;height:849px;overflow:hidden;background:var(--bg)}
  body{font-family:"Montserrat",sans-serif;position:relative}

  .tube{position:absolute;left:40px;width:1120px;height:270px}
  .tube--front{top:70px}
  .tube--back{top:500px}
  .tube-shape{position:absolute;inset:0;width:1120px;height:270px}

  .layer{position:absolute}
  .texture{position:absolute;border-radius:2px}

  /* front */
  .front-texture{left:16px;top:0;width:270px;height:270px;
    background:linear-gradient(120deg,var(--blue-mist),var(--blue-pale) 50%,var(--white))}
  .brand-block{left:300px;top:78px;width:310px;text-align:center}
  .brand-mark{display:flex;align-items:center;justify-content:center;gap:10px}
  .brand-dot{width:16px;height:16px;border-radius:50%;background:var(--white)}
  .brand-name{font-weight:900;font-size:44px;color:var(--white);letter-spacing:-1px;line-height:1}
  .brand-tag{margin-top:26px;font-weight:800;font-size:16px;color:var(--ink);letter-spacing:.5px}

  .claims{left:630px;top:30px;width:300px;height:120px;border:1.5px solid rgba(255,255,255,.7);padding:16px 18px}
  .claims li{list-style:none;font-weight:700;font-size:13px;line-height:1.2;margin-bottom:10px;padding-left:14px;position:relative;text-transform:uppercase}
  .claims li::before{content:"";position:absolute;left:0;top:5px;width:7px;height:7px;border-radius:50%;background:currentColor}
  .claims .claim-dark{color:#1c2a36}
  .claims .claim-light{color:#b9cfdc}

  .strength{left:630px;top:162px;width:192px;height:88px;background:linear-gradient(180deg,var(--blue-primary),var(--blue-deep));padding:10px 14px;color:var(--white)}
  .strength-code{font-weight:900;font-size:42px;line-height:1}
  .strength-ppm{font-weight:700;font-size:13px;color:var(--blue-pale);margin-top:6px}

  .flavour{left:840px;top:150px;width:62px;height:62px;border-radius:50%;background:var(--blue-mist);border:4px solid var(--blue-primary);text-align:center;padding-top:11px;font-weight:800;font-size:11px;line-height:1.1;color:var(--blue-deep)}
  .flavour-leaf{left:862px;top:196px;width:40px;height:28px;border-radius:50%;background:linear-gradient(135deg,#3fa660,#1c6b3a)}
  .net-weight{left:840px;top:234px;font-weight:800;font-size:13px;color:#a7c3d3;white-space:nowrap}

  /* back */
  .back-texture{left:16px;top:0;width:300px;height:270px;
    background:linear-gradient(120deg,var(--white),var(--blue-pale) 55%,var(--blue-mist))}
  .headline{left:330px;top:24px;background:var(--ink);color:var(--white);padding:6px 12px;border-radius:4px}
  .headline-main{font-weight:900;font-size:24px;line-height:1}
  .headline-sub{font-weight:800;font-size:12px;letter-spacing:.6px;margin-top:3px}
  .benefits{left:660px;top:22px}
  .benefits li{list-style:none;font-weight:700;font-style:italic;font-size:15px;line-height:1.2;color:var(--white);margin-bottom:4px;padding-left:14px;position:relative}
  .benefits li::before{content:"";position:absolute;left:0;top:6px;width:7px;height:7px;border-radius:50%;background:var(--white)}
  .illustration{top:96px;width:92px;height:92px;border-radius:50%;border:5px solid var(--blue-deep);
    background:radial-gradient(circle,#f7c6c6 0 40%,var(--blue-mist) 41%)}
  .illustration--braces{left:340px}
  .illustration--aligners{left:450px}

  .info{left:600px;top:100px;width:330px;height:150px;background:rgba(233,246,251,.85);padding:10px 12px;color:#1e2c38;font-size:9.5px;line-height:1.3}
  .info h3{font-size:10px;font-weight:800;font-style:italic}
  .info p{font-style:italic;font-weight:500;margin-bottom:5px}
  .directions{left:340px;top:198px;width:245px;font-size:9.5px;line-height:1.3;color:#1e2c38}
  .directions h3{font-size:10px;font-weight:800;font-style:italic}
  .directions p{font-style:italic;font-weight:500}
</style>
</head>
<body>

<section class="tube tube--front" aria-label="Front of tube">
  <svg class="tube-shape" viewBox="0 0 1120 270" aria-hidden="true">
    <defs>
      <linearGradient id="bodyFront" x1="0" y1="0" x2="0" y2="1">
        <stop offset="0" stop-color="#00a9dd"/>
        <stop offset=".5" stop-color="#0094d4"/>
        <stop offset="1" stop-color="#0b5f8f"/>
      </linearGradient>
      <linearGradient id="capFront" x1="0" y1="0" x2="0" y2="1">
        <stop offset="0" stop-color="#c7ebf8"/>
        <stop offset="1" stop-color="#6fccea"/>
      </linearGradient>
    </defs>
    <rect x="0" y="0" width="16" height="270" fill="#6fccea"/>
    <rect x="16" y="0" width="930" height="270" fill="url(#bodyFront)"/>
    <polygon points="946,0 1010,95 1010,175 946,270" fill="#0b6fa3"/>
    <rect x="1010" y="80" width="110" height="110" rx="6" fill="url(#capFront)"/>
  </svg>

  <div class="texture front-texture" role="img" aria-label="Icy crystal texture in pale blue and white"></div>

  <div class="layer brand-block">
    <div class="brand-mark">
      <span class="brand-dot"></span>
      <span class="brand-name">quorlume</span>
    </div>
    <p class="brand-tag">ORTHODONTIC TOOTHPASTE</p>
  </div>

  <ul class="layer claims">
    <li class="claim-dark">Enhanced cavity prevention and gum protection</li>
    <li class="claim-light">For use when wearing metal braces and clear aligners</li>
  </ul>

  <div class="layer strength">
    <p class="strength-code">Q2786</p>
    <p class="strength-ppm">Fluoride 1450 ppm</p>
  </div>

  <div class="layer flavour">Double<br>Mint</div>
  <div class="layer flavour-leaf" role="img" aria-label="Mint leaf illustration"></div>
  <p class="layer net-weight">NET WT. 85g</p>
</section>

<section class="tube tube--back" aria-label="Back of tube">
  <svg class="tube-shape" viewBox="0 0 1120 270" aria-hidden="true">
    <defs>
      <linearGradient id="bodyBack" x1="0" y1="0" x2="0" y2="1">
        <stop offset="0" stop-color="#0b5f8f"/>
        <stop offset=".45" stop-color="#0094d4"/>
        <stop offset="1" stop-color="#00a9dd"/>
      </linearGradient>
      <linearGradient id="capBack" x1="0" y1="0" x2="0" y2="1">
        <stop offset="0" stop-color="#c7ebf8"/>
        <stop offset="1" stop-color="#6fccea"/>
      </linearGradient>
    </defs>
    <rect x="0" y="0" width="16" height="270" fill="#6fccea"/>
    <rect x="16" y="0" width="930" height="270" fill="url(#bodyBack)"/>
    <polygon points="946,0 1010,95 1010,175 946,270" fill="#0b6fa3"/>
    <rect x="1010" y="80" width="110" height="110" rx="6" fill="url(#capBack)"/>
  </svg>

  <div class="texture back-texture" role="img" aria-label="Icy crystal texture in pale blue and white"></div>

  <div class="layer headline">
    <p class="headline-main">PREMIUM ORAL CARE</p>
    <p class="headline-sub">DURING ORTHODONTIC TREATMENT</p>
  </div>

  <ul class="layer benefits">
    <li>Prevent Cavity</li>
    <li>Freshen Breath</li>
    <li>Strengthen Teeth</li>
  </ul>

  <div class="layer illustration illustration--braces" role="img" aria-label="Smile with metal braces illustration"></div>
  <div class="layer illustration illustration--aligners" role="img" aria-label="Smile with clear aligners illustration"></div>

  <div class="layer directions">
    <h3>Directions</h3>
    <p>Apply at least one inch strip of the product onto a soft bristle toothbrush. Brush teeth thoroughly, for at least three minutes twice a day.</p>
  </div>

  <div class="layer info">
    <h3>Ingredients:</h3>
    <p>Aqua, Sorbitol, Hydrated Silica, Glycerin, PEG-12, Sodium Lauryl Sulfate, Aroma, Cellulose Gum, Titanium Dioxide, Potassium Sorbate, Allantoin, Sodium Fluoride, Citric Acid, Peppermint Essence, Sodium Saccharin, CI 47005, CI 42090, Cinnamal.</p>
    <h3>Warnings:</h3>
    <p>Do not ingest. Keep out of reach of children under 6 years of age.</p>
  </div>
</section>

</body>
</html>
```